Flyer Design Project

I am opening a yoga studio called Willowmere Yoga .Pilates. Fitness
and require a flyer that will be letterbox dropped. It will two sided - DL size.100mm × 210mm

The studio will offer Vinyasa Flow Yoga and Mat Pilates classes. We aim to enable people to lead healthier, happier lives through improved strength, flexibility and general well being that regular yoga and pilates practice offers.

We offer group classes, private and semi private sessions in yoga and pilates.

it must have the logo on it- I have uploaded the logo in two versions - not sure what will look the best.

pick up one of the colours from the logo as the background colour.

Side one:
Simple and clean with one side showing logo and address details, website and with simple intro about studio (if it fits)

Location: 1st Floor, 17 Larkspur Parade, Tindale, 3286
phone: 0428 596143
www.willowmeretindale.com.au

OPENING OCTOBER

other side - class descriptions and intro offer for new clients
$20 for 7 days of classes
$99 for 1 month unlimited.

Class descriptions:
Vinyasa Flow yoga: A class that flows from pose to pose integrating breath, alignment, strength and power. All levels are catered for in a warm room heated to around 26 degrees. You will leave feeling inspired, empowered and energised.

Mat Pilates: A strong, challenging class integrating the key principles of pilates: concentration, control, centring, precision, flowing movement and breath. Using the core as a focus to develop these principles you will be hooked on the physical freedom you experience post workout:improved strength, flexibility and vitality that pilates offers.

Private and semi Private tuition available.

Target Market(s)

mainly women, athletic, 35-55 age, middle class, well educated

Industry/Entity Type

Fitness

Requirements
Must have
• 2 pages
the logo

Should not have
• no pics

```html
<!DOCTYPE html>
<html lang="en">
<head>
<meta charset="utf-8">
<title>Willowmere Yoga — DL Flyer</title>
<link href="https://fonts.googleapis.com/css2?family=PT+Sans:ital,wght@0,400;0,700;1,400;1,700&family=Black+Ops+One&display=swap" rel="stylesheet">
<style>
  :root {
    --page: #ffffff;
    --ink: #111111;
    --brand-grey: #58595b;
    --sky: #1ab8e6;
    --sky-pale: #eaf8fd;
    --border: #222222;
    --pill-text: #ffffff;
  }
  * { box-sizing: border-box; margin: 0; padding: 0; }
  html, body { width: 1200px; height: 848px; overflow: hidden; background: var(--page); }
  body { position: relative; font-family: "PT Sans", Arial, sans-serif; color: var(--ink); }

  .flyer-side {
    position: absolute;
    top: 88px;
    width: 284px;
    height: 596px;
    border: 1px solid var(--border);
    background: linear-gradient(to bottom, var(--page) 0%, var(--page) 32%, var(--sky-pale) 50%, var(--sky) 100%);
  }
  .flyer-side--front { left: 207px; }
  .flyer-side--back { left: 646px; }

  /* Front */
  .brand {
    position: absolute; left: 12px; top: 20px; width: 258px; height: 162px;
    display: flex; flex-direction: column; align-items: center; justify-content: center; gap: 12px;
  }
  .brand-dot { width: 58px; height: 58px; border-radius: 50%; background: var(--sky); }
  .brand-name {
    font-weight: 700; font-size: 19px; color: var(--brand-grey);
    text-align: center; line-height: 1.2; letter-spacing: 0.5px;
  }
  .address { position: absolute; top: 200px; width: 100%; text-align: center; font-size: 18px; line-height: 24px; }
  .phone {
    position: absolute; top: 256px; width: 100%; display: flex; justify-content: center; align-items: center; gap: 6px;
    font-size: 21px; font-weight: 700;
  }
  .phone svg { width: 14px; height: 18px; }
  .website { position: absolute; top: 290px; width: 100%; text-align: center; font-size: 15px; font-weight: 700; font-style: italic; }
  .intro { position: absolute; left: 17px; top: 350px; width: 250px; font-size: 12.6px; line-height: 16.4px; text-align: justify; }
  .intro p + p { margin-top: 16px; }
  .opening {
    position: absolute; top: 536px; width: 100%; text-align: center;
    font-family: "Black Ops One", "Arial Black", sans-serif; font-size: 26px; letter-spacing: 0.5px; color: var(--ink);
  }

  /* Back */
  .pill {
    position: absolute; left: 9px; height: 24px; padding: 0 10px 0 14px; border-radius: 12px;
    background: var(--sky); color: var(--pill-text);
    font-weight: 700; font-style: italic; font-size: 15.5px; line-height: 24px;
  }
  .pill--offer { top: 30px; width: 212px; }
  .pill--vinyasa { top: 154px; width: 156px; padding-left: 8px; }
  .pill--pilates { top: 317px; width: 154px; padding-left: 8px; }
  .offer { position: absolute; left: 33px; top: 60px; font-weight: 700; font-size: 18.5px; line-height: 27px; }
  .class-copy { position: absolute; left: 16px; width: 249px; font-size: 12.6px; line-height: 16.9px; text-align: justify; text-indent: 10px; }
  .class-copy--vinyasa { top: 187px; }
  .class-copy--pilates { top: 346px; }
  .tuition { position: absolute; left: 26px; top: 512px; font-size: 12.6px; }
</style>
</head>
<body>
  <section class="flyer-side flyer-side--front" aria-label="Flyer front">
    <div class="brand">
      <span class="brand-dot"></span>
      <span class="brand-name">Willowmere Yoga<br>.Pilates. Fitness</span>
    </div>
    <p class="address">1st Floor, 17 Larkspur Parade,<br>Tindale, 3286</p>
    <p class="phone">
      <svg viewBox="0 0 14 18" aria-hidden="true"><path d="M3 1 L6 4.5 L4.4 6.6 C5 9 6.5 11.4 8.6 12.8 L10.6 11.4 L13.5 14.5 L11.4 16.8 C6 16 1.4 9.6 1.2 3.2 Z" fill="#111"/></svg>
      0428 596143
    </p>
    <p class="website">www.willowmeretindale.com.au</p>
    <div class="intro">
      <p>The studio will offer Vinyasa Flow Yoga and Mat Pilates classes. We aim to enable people to lead healthier, happier lives through improved strength, flexibility and general well being that regular yoga and pilates practice offers.</p>
      <p>We offer group classes, private and semi private sessions in yoga and pilates.</p>
    </div>
    <p class="opening">OPENING OCTOBER</p>
  </section>

  <section class="flyer-side flyer-side--back" aria-label="Flyer back">
    <h2 class="pill pill--offer">Intro offer for new clients:</h2>
    <p class="offer">$20 for 7 days of classes<br>$99 for 1 month unlimited</p>

    <h2 class="pill pill--vinyasa">Vinyasa Flow yoga:</h2>
    <p class="class-copy class-copy--vinyasa">A class that flows from pose to pose integrating breath, alignment, strength and power. All levels are catered for in a warm room heated to around 26 degrees. You will leave feeling inspired, empowered and energised.</p>

    <h2 class="pill pill--pilates">Mat Pilates:</h2>
    <p class="class-copy class-copy--pilates">A strong, challenging class integrating the key principles of pilates: concentration, control, centring, precision, flowing movement and breath. Using the core as a focus to develop these principles you will be hooked on the physical freedom you experience post workout:improved strength, flexibility and vitality that pilates offers.</p>

    <p class="tuition">Private and semi Private tuition available.</p>
  </section>
</body>
</html>
```